Rebrand of 3 bottle labels for nail polish brand

The task is to make a rebranding of our current gel nail polish bottle design. We have become one of the leading european nail polish brand, so we want to improve the quality of the label design to a more scandinavian and minimalistic bottle design, which stille has to be recognisable and unique.

We have attached a more detailed description of the rebranding instructions for our gel polish bottles called "bottle task".
Updates

The Labels should not be just Black and White as stated. But should be mainly Black and White and then some of our color as explained in the uploaded file.

Target Market(s)

Girls and women age 18-55 Northern Europe

Industry/Entity Type

Cosmetic/ Nail Gel Polish

Colors

Designer to choose only greyscale colors for use in the design.

Requirements
Must have
• See attched design instruction
Nice to have
• Moderne, Minimalist, Recognizable and Unique look
Should not have
• Too many elements, too busy design

```html
<!DOCTYPE html>
<html lang="en">
<head>
<meta charset="utf-8">
<title>Halden Base Coat Label</title>
<link href="https://fonts.googleapis.com/css2?family=Poppins:wght@400;500;600;700&display=swap" rel="stylesheet">
<style>
  :root {
    --page: #ffffff;
    --label-black: #1c1b1b;
    --ink-white: #ffffff;
    --ink-grey: #b8b6b5;
    --rule-grey: #5a5857;
    --blush: #c8a398;
    --blush-dark: #2a2120;
  }
  * { margin: 0; padding: 0; box-sizing: border-box; }
  html, body { width: 883px; height: 1200px; overflow: hidden; background: var(--page); }
  body { position: relative; font-family: 'Poppins', sans-serif; }

  .label {
    position: absolute; left: 15px; top: 486px;
    width: 853px; height: 227px;
    background: var(--label-black);
    box-shadow: 0 4px 8px rgba(0,0,0,0.25);
  }
  .label__band {
    position: absolute; left: 0; bottom: 0; width: 100%; height: 5px;
    background: var(--blush);
  }

  .front { position: absolute; left: 117px; top: 0; width: 152px; text-align: center; color: var(--ink-white); }
  .brand {
    position: absolute; left: -40px; top: 34px; width: 232px;
    font-weight: 600; font-size: 28px; line-height: 1; letter-spacing: 7px;
    padding-left: 7px;
  }
  .rule { position: absolute; left: 0; width: 152px; height: 1px; background: var(--rule-grey); }
  .rule--top { top: 88px; }
  .rule--mid { top: 116px; }
  .rule--bottom { top: 187px; }
  .product-name { position: absolute; left: 0; top: 92px; width: 100%; font-weight: 700; font-size: 16px; line-height: 20px; }
  .product-type { position: absolute; left: -10px; top: 122px; width: 172px; font-weight: 400; font-size: 8.5px; letter-spacing: 3px; color: var(--ink-grey); }
  .volume { position: absolute; left: 26px; top: 151px; display: flex; align-items: center; gap: 4px; font-size: 10.5px; }
  .volume__number {
    width: 26px; height: 26px; border-radius: 50%; background: var(--blush);
    color: var(--blush-dark); font-weight: 700; font-size: 12px; line-height: 26px; text-align: center;
  }
  .finish { position: absolute; left: 30px; top: 196px; font-size: 10px; font-weight: 600; letter-spacing: 2.5px; }
  .badge { position: absolute; left: 120px; top: 181px; width: 32px; height: 32px; border-radius: 50%; border: 1.5px solid var(--ink-grey); }

  .info { position: absolute; left: 445px; top: 22px; width: 335px; color: var(--ink-white); font-size: 6.4px; line-height: 8px; }
  .info p { margin-bottom: 14px; text-align: justify; }
  .info strong { font-weight: 700; }

  .footer { position: absolute; left: 445px; top: 178px; width: 335px; height: 26px; color: var(--ink-white); }
  .address { position: absolute; left: 0; top: 2px; font-size: 6px; line-height: 7.5px; color: var(--ink-grey); }
  .footer__divider { position: absolute; left: 110px; top: 0; width: 1px; height: 28px; background: var(--rule-grey); }
  .origin { position: absolute; left: 125px; top: 6px; font-size: 9.5px; font-weight: 500; }
  .marks { position: absolute; left: 211px; top: 0; display: flex; gap: 6px; }
  .marks span { width: 26px; height: 26px; border-radius: 50%; border: 1.2px solid var(--ink-white); }
</style>
</head>
<body>
  <section class="label" aria-label="Halden Base Coat bottle label">
    <div class="front">
      <div class="brand">HALDEN</div>
      <div class="rule rule--top"></div>
      <div class="product-name">BASE COAT</div>
      <div class="rule rule--mid"></div>
      <div class="product-type">SOAK OFF UV/LED</div>
      <div class="volume"><span class="volume__number">01</span><span>15ml ℮ 0.5oz</span></div>
      <div class="rule rule--bottom"></div>
      <div class="finish">FLEXIBLE</div>
      <div class="badge" aria-hidden="true"></div>
    </div>

    <div class="info">
      <p><strong>DIRECTIONS FOR USE (ENG):</strong> Halden Base Coat must be applied in thin layers and cured in one of our Halden Lamps. See instructions for more information.</p>
      <p><strong>ANVENDELSE (DK):</strong> Halden Base Coat skal påføres i tynde lag og hærdes i en af vores Halden Lamper. Se instruktioner for mere information</p>
      <p><strong>CAUTION (ENG):</strong> Keep out of reach of children. Discontinue use if irritation occurs. Avoid direct sunlight or extreme exposure to LED or UV light.</p>
      <p><strong>ADVARSEL (DK):</strong> Opbevar utilgængeligt for børn. Stop din behandling, hvis produktet forudsager irritation. Undgå direkte sollys eller udsættelse for LED eller UV.</p>
      <p><strong>INGREDIENTS:</strong> Acrylates Copolymer, Acrylated Aliphatic Urethane, Cellulose Acetate Butanoate, Dimethicone, Ceresine, wax, Pigment Red, Carbon Black, Titanium dioxide, CI 77891</p>
    </div>

    <div class="footer">
      <div class="address">Brightfold ApS - Solbjerg<br>Havnegade 14C 4100 Solbjerg,<br>Denmark</div>
      <div class="footer__divider"></div>
      <div class="origin">Made in Europe</div>
      <div class="marks" aria-hidden="true"><span></span><span></span><span></span><span></span></div>
    </div>

    <div class="label__band"></div>
  </section>
</body>
</html>
```